Logo + Label Design (Men’s Grooming Brand & Product Packaging)

Design a logo and 2 oz pomade label for Brant, a modern men’s grooming brand focused on clean, high-quality, natural ingredients. The design should establish a bold, masculine, minimalist identity that can later extend to products like shaving gel and body wash.

Key Requirements

Create a primary logo for “Brant” and a core label for the 2 oz pomade jar (screw-top).

Use a clean, modern style — masculine, confident, and approachable (think Wendel’s, Valto, Northfield Mill).

Design for 1–2 color screen printing on solid jar colors (white, black, or navy).

Avoid gradients, foil, or embossing. Must work in black & white.

Provide: vector logo, mockup of the 2 oz jar, color palette (CMYK/RGB/HEX), and font specs.

Winning design may lead to future projects (body wash, shave gel, skincare lines).

Font styles to use
Other font styles liked:
• We like the fonts and design concept in the attached mockup.

Requirements
Should not have
• We want to avoid too much writing or busy designs. We want to avoid having graphics/illustrations embedded in the logo if they will cause the brand to look less classy or sophisticated. We also want the design to look simple and all-American (e.g. Pellham and Stroud, Tall Pine, The BRIM, etc). We’d like to give a Kessler & Dunmore vibe that feels classy and high end.

```html
<!DOCTYPE html>
<html lang="en">
<head>
<meta charset="utf-8">
<title>Brant Pomade Label</title>
<link rel="stylesheet" href="https://fonts.googleapis.com/css2?family=Oswald:wght@300;400&family=Playfair+Display:wght@400;700&display=swap">
<style>
  :root {
    --label-black: #000000;
    --label-white: #ffffff;
    --page-bg: #ffffff;
  }
  html, body {
    margin: 0;
    padding: 0;
    width: 1199px;
    height: 1200px;
    overflow: hidden;
    background: var(--page-bg);
  }
  .jar-label {
    display: block;
    width: 1199px;
    height: 1200px;
  }
  .label-disc { fill: var(--label-black); }
  .label-ring { fill: none; stroke: var(--label-white); stroke-width: 2.5; }
  .brand-name {
    font-family: "Playfair Display", serif;
    font-weight: 400;
    font-size: 230px;
    fill: var(--label-white);
  }
  .product-name {
    font-family: "Playfair Display", serif;
    font-weight: 700;
    font-size: 74px;
    letter-spacing: 0.24em;
    fill: var(--label-white);
  }
  .scent-name {
    font-family: "Oswald", sans-serif;
    font-weight: 300;
    font-size: 54px;
    letter-spacing: 0.2em;
    fill: var(--label-white);
  }
  .hold-finish {
    font-family: "Oswald", sans-serif;
    font-weight: 400;
    font-size: 52px;
    fill: var(--label-white);
  }
  .net-weight {
    font-family: "Oswald", sans-serif;
    font-weight: 300;
    font-size: 36px;
    fill: var(--label-white);
  }
</style>
</head>
<body>
<svg class="jar-label" viewBox="0 0 1199 1200" xmlns="http://www.w3.org/2000/svg" role="img" aria-label="Brant pomade jar lid label">
  <circle class="label-disc" cx="599.5" cy="604" r="566"/>
  <circle class="label-ring" cx="599.5" cy="604" r="492"/>

  <text class="brand-name" x="599.5" y="450" text-anchor="middle">Brant</text>

  <text class="product-name" x="608" y="672" text-anchor="middle">POMADE</text>
  <text class="scent-name" x="605" y="740" text-anchor="middle">FRESH &amp; CLEAN</text>
  <text class="hold-finish" x="599.5" y="842" text-anchor="middle">MEDIUM HOLD – MATTE FINISH</text>
  <text class="net-weight" x="599.5" y="992" text-anchor="middle">NET WT 2 oz (57g)</text>
</svg>
</body>
</html>
```